Visitenkarten-Design für Osteopathie-Praxis
Zielgruppe
Es handelt sich um eine Osteopathie-Praxis mit einer eher gehobenen (preislich) Zielgruppe mit allen Altersklassen. Die Praxis soll im leichten skandinavischen Stil eingerichtet werden und die Internetseite mit folgenden Theme entworfen werden: http://demo.pixelhaus-vorlagen.de/#pv_merle
Aufgabenstellung
Das Design muss leicht und klar sein. Es darf nicht überlastet sein. Auf die Vorderseite soll das Logo kommen und auf die Rückseite die Kontaktdaten sowie die Leistungen (Osteopath D.O., Physiotherapeut, Heilpraktiker) und meinen Name. Ich habe Beispiele zugefügt. Das Logo besteht nur aus dem Kreis. Als Text soll 'Vitalis - Osteopathische Medizin' zum Logo kommen dabei sollte einen Font genutzt werden den ich auf der Internetseite wieder nutzen kann.

```html
<!DOCTYPE html>
<html lang="de">
<head>
<meta charset="utf-8">
<title>Vitalis – Osteopathische Medizin · Visitenkarten</title>
<link rel="stylesheet" href="https://fonts.googleapis.com/css2?family=Marcellus&family=Questrial&family=Fira+Sans:wght@300;400&display=swap">
<style>
  :root {
    --board: #2b2b2b;
    --paper: #ffffff;
    --card-white: #f4f4f3;
    --navy: #0c1a2e;
    --teal: #7cc3ca;
    --teal-light: #a9d8dc;
    --ink: #3a3d40;
    --ink-soft: #5b5f63;
    --scene: #3b3937;
  }
  * { box-sizing: border-box; margin: 0; padding: 0; }
  html, body { width: 795px; height: 1200px; overflow: hidden; }
  body { background: var(--board); position: relative; font-family: "Fira Sans", sans-serif; color: var(--ink); }

  .panel { position: absolute; left: 88px; width: 620px; }
  .panel--logo { top: 83px; height: 264px; background: var(--paper); }
  .panel--cards { top: 347px; height: 330px; background: var(--navy); }
  .panel--scene { top: 677px; height: 436px; background: var(--scene); }

  /* brand lockup */
  .brand { position: absolute; left: 0; width: 100%; text-align: center; }
  .brand__dot { display: block; margin: 0 auto; border-radius: 50%; background: var(--teal); }
  .brand__name { font-family: "Marcellus", serif; font-weight: 400; color: var(--ink); text-transform: uppercase; }
  .brand__tagline { font-family: "Questrial", sans-serif; color: var(--ink); text-transform: uppercase; }

  .panel--logo .brand { top: 71px; }
  .panel--logo .brand__dot { width: 62px; height: 62px; }
  .panel--logo .brand__name { margin-top: 14px; font-size: 29px; letter-spacing: 15px; padding-left: 15px; line-height: 32px; }
  .panel--logo .brand__tagline { margin-top: 4px; font-size: 10px; letter-spacing: 4.2px; padding-left: 4px; }

  /* cards */
  .card { position: absolute; width: 118px; height: 180px; box-shadow: 0 6px 10px rgba(0,0,0,.55); overflow: hidden; }
  .card--teal { background: var(--teal); }
  .card--white { background: var(--card-white); }
  .card__rule { position: absolute; left: 50%; width: 0.6px; background: var(--teal); }
  .card--teal .card__rule { background: var(--teal-light); }

  .card-front .card__rule--full { top: 0; height: 100%; }
  .card-front .card__mark { position: absolute; left: 50%; top: 50%; width: 42px; height: 42px; margin: -21px 0 0 -21px; border-radius: 50%; background: var(--teal); display: flex; align-items: center; justify-content: center; }
  .card--teal .card__mark { background: var(--teal-light); }
  .card-front .card__mark span { font-family: "Marcellus", serif; font-size: 6px; letter-spacing: 1.6px; color: var(--paper); text-transform: uppercase; padding-left: 1.6px; }

  .card-back .card__rule--top { top: 0; height: 13px; }
  .card-back .card__rule--bottom { bottom: 0; height: 11px; }
  .card-back .brand { top: 16px; }
  .card-back .brand__dot { width: 26px; height: 26px; }
  .card-back .brand__name { margin-top: 5px; font-size: 12px; letter-spacing: 5px; padding-left: 5px; line-height: 13px; }
  .card-back .brand__tagline { margin-top: 2px; font-size: 4.4px; letter-spacing: 1.5px; padding-left: 1.5px; }
  .contact { position: absolute; left: 0; top: 85px; width: 100%; text-align: center; }
  .contact__name { font-weight: 300; font-size: 7px; letter-spacing: .2px; color: var(--teal); text-transform: uppercase; }
  .contact__roles { margin-top: 2px; font-size: 4.4px; color: var(--ink-soft); }
  .contact__roles i { font-style: normal; color: var(--teal); padding: 0 1px; }
  .contact__sep { display: block; width: 2px; height: 2px; margin: 5px auto 4px; border-radius: 50%; background: var(--teal); }
  .contact__line { font-size: 4.4px; line-height: 6px; color: var(--ink-soft); }

  /* larger presentation in lower section */
  .scene-back { left: 120px; top: 90px; transform: scale(1.35); transform-origin: top left; }
  .card--landscape { width: 250px; height: 160px; }
  .card--landscape .card__rule--across { position: absolute; top: 50%; left: 0; width: 100%; height: 0.6px; background: var(--teal-light); }
  .scene-front { left: 320px; top: 40px; }
  .card--landscape .card__mark { width: 56px; height: 56px; margin: -28px 0 0 -28px; }
  .card--landscape .card__mark span { font-size: 7.5px; letter-spacing: 2px; padding-left: 2px; }
</style>
</head>
<body>

  <section class="panel panel--logo">
    <div class="brand">
      <span class="brand__dot"></span>
      <h1 class="brand__name">Vitalis</h1>
      <p class="brand__tagline">Osteopathische Medizin</p>
    </div>
  </section>

  <section class="panel panel--cards">
    <div class="card card--teal card-front" style="left:32px; top:67px;">
      <span class="card__rule card__rule--full"></span>
      <div class="card__mark"><span>Vitalis</span></div>
    </div>

    <div class="card card--white card-back" style="left:172px; top:67px;">
      <span class="card__rule card__rule--top"></span>
      <div class="brand">
        <span class="brand__dot"></span>
        <p class="brand__name">Vitalis</p>
        <p class="brand__tagline">Osteopathische Medizin</p>
      </div>
      <div class="contact">
        <p class="contact__name">Matthias Kellner</p>
        <p class="contact__roles">Osteopath D.O. <i>|</i> Physiotherapeut <i>|</i> Heilpraktiker</p>
        <span class="contact__sep"></span>
        <p class="contact__line">Lindenhofweg 8</p>
        <p class="contact__line">72108 Rottenburg</p>
        <span class="contact__sep"></span>
        <p class="contact__line">T. +49 711 2094 3317</p>
        <span class="contact__sep"></span>
        <p class="contact__line">info@vitalis-osteo.de</p>
        <p class="contact__line">www.vitalis-osteo.de</p>
      </div>
      <span class="card__rule card__rule--bottom"></span>
    </div>

    <div class="card card--white card-front" style="left:325px; top:67px;">
      <span class="card__rule card__rule--full"></span>
      <div class="card__mark"><span>Vitalis</span></div>
    </div>

    <div class="card card--white card-back" style="left:464px; top:67px;">
      <span class="card__rule card__rule--top"></span>
      <div class="brand">
        <span class="brand__dot"></span>
        <p class="brand__name">Vitalis</p>
        <p class="brand__tagline">Osteopathische Medizin</p>
      </div>
      <div class="contact">
        <p class="contact__name">Matthias Kellner</p>
        <p class="contact__roles">Osteopath D.O. <i>|</i> Physiotherapeut <i>|</i> Heilpraktiker</p>
        <span class="contact__sep"></span>
        <p class="contact__line">Lindenhofweg 8</p>
        <p class="contact__line">72108 Rottenburg</p>
        <span class="contact__sep"></span>
        <p class="contact__line">T. +49 711 2094 3317</p>
        <span class="contact__sep"></span>
        <p class="contact__line">info@vitalis-osteo.de</p>
        <p class="contact__line">www.vitalis-osteo.de</p>
      </div>
      <span class="card__rule card__rule--bottom"></span>
    </div>
  </section>

  <section class="panel panel--scene">
    <div class="card card--teal card-front card--landscape scene-front">
      <span class="card__rule--across"></span>
      <div class="card__mark"><span>Vitalis</span></div>
    </div>

    <div class="card card--white card-back scene-back">
      <span class="card__rule card__rule--top"></span>
      <div class="brand">
        <span class="brand__dot"></span>
        <p class="brand__name">Vitalis</p>
        <p class="brand__tagline">Osteopathische Medizin</p>
      </div>
      <div class="contact">
        <p class="contact__name">Matthias Kellner</p>
        <p class="contact__roles">Osteopath D.O. <i>|</i> Physiotherapeut <i>|</i> Heilpraktiker</p>
        <span class="contact__sep"></span>
        <p class="contact__line">Lindenhofweg 8</p>
        <p class="contact__line">72108 Rottenburg</p>
        <span class="contact__sep"></span>
        <p class="contact__line">T. +49 711 2094 3317</p>
        <span class="contact__sep"></span>
        <p class="contact__line">info@vitalis-osteo.de</p>
        <p class="contact__line">www.vitalis-osteo.de</p>
      </div>
      <span class="card__rule card__rule--bottom"></span>
    </div>
  </section>

</body>
</html>
```